Business Card Design

We are looking for a business card designed for our landscaping company. We do landscaping installation & Maintenance Services. We would like to see designs that have basic landscaping in background. We also think it is important to have both of our names and phone numbers on the card. We need something that stands out a little whether it is shape of the card or thickness or design.

Industry/Entity Type

Business

Contact Information for Business Card

Prairie Oak Yardworks, prairieoakyard@mailbox-demo.net, Dale Pruitt 555-613-2907, Marcus Delgado 555-287-4163

```html
<!DOCTYPE html>
<html lang="en">
<head>
<meta charset="utf-8">
<title>Prairie Oak Yardworks – Business Card</title>
<link href="https://fonts.googleapis.com/css2?family=Carlito:wght@400;700&display=swap" rel="stylesheet">
<style>
  :root {
    --leaf: #6ab150;
    --leaf-soft: rgba(106, 177, 80, 0);
    --paper: #ffffff;
    --backdrop: #e8e5e0;
  }
  html, body {
    margin: 0;
    padding: 0;
    width: 1200px;
    height: 1008px;
    overflow: hidden;
    background: var(--backdrop);
  }
  .business-card {
    position: absolute;
    left: 80px;
    top: 187px;
    width: 1040px;
    height: 634px;
    background: var(--paper);
    box-shadow: 0 14px 30px rgba(0, 0, 0, 0.25);
  }
  .card-art {
    display: block;
    width: 100%;
    height: 100%;
    font-family: "Carlito", "Calibri", sans-serif;
  }
  .green-field { fill: var(--leaf); }
  .white-wave { fill: var(--paper); filter: url(#wave-shadow); }
  .swoosh-green { fill: var(--leaf); }
  .swoosh-white { fill: var(--paper); }
  .company-name { fill: var(--leaf); font-weight: 700; font-size: 27px; }
  .email-text { fill: var(--leaf); font-weight: 400; font-size: 20px; }
  .email-icon { fill: var(--leaf); }
  .email-glyph { fill: none; stroke: var(--paper); stroke-width: 1.4; }
  .person-name { fill: var(--paper); font-weight: 700; font-size: 27px; }
  .phone-number { fill: var(--paper); font-weight: 700; font-size: 26px; }
  .phone-ring { fill: none; stroke: var(--paper); stroke-width: 1.8; }
  .phone-handset { fill: var(--paper); }
  .plant-area { fill: url(#plant-fade); }
</style>
</head>
<body>
  <div class="business-card">
    <svg class="card-art" viewBox="0 0 802 489" xmlns="http://www.w3.org/2000/svg">
      <defs>
        <filter id="wave-shadow" x="-10%" y="-10%" width="130%" height="130%">
          <feDropShadow dx="6" dy="4" stdDeviation="6" flood-color="#000" flood-opacity="0.35"/>
        </filter>
        <linearGradient id="plant-fade" x1="0" y1="1" x2="0" y2="0">
          <stop offset="0" stop-color="#6ab150" stop-opacity="1"/>
          <stop offset="0.35" stop-color="#6ab150" stop-opacity="0.75"/>
          <stop offset="1" stop-color="#6ab150" stop-opacity="0.08"/>
        </linearGradient>
      </defs>

      <rect class="green-field" x="0" y="0" width="802" height="489"/>
      <path class="white-wave" d="M0,0 L655,0 C672,40 650,92 560,122 C450,160 300,182 222,280 C172,345 176,430 190,489 L0,489 Z"/>

      <path class="swoosh-green" d="M37,168 C-10,120 20,30 180,14 C260,8 320,30 348,62 C300,35 240,22 180,26 C60,38 10,110 37,168 Z"/>
      <path class="swoosh-white" d="M452,424 C560,480 760,490 792,410 C800,380 785,340 765,320 C790,360 790,400 750,430 C680,475 540,465 452,424 Z"/>

      <rect class="plant-area" role="img" aria-label="Silhouette of tall grass and a cattail plant"
            x="14" y="245" width="118" height="244"/>

      <text class="company-name" x="59" y="97">Prairie Oak Yardworks</text>
      <circle class="email-icon" cx="70" cy="144" r="9"/>
      <path class="email-glyph" d="M64,140 h12 v8 h-12 Z M64,140 l6,5 l6,-5"/>
      <text class="email-text" x="86" y="151">prairieoakyard@mailbox-demo.net</text>

      <text class="person-name" x="495" y="234">Dale Pruitt</text>
      <g class="phone-icon" transform="translate(506,266)">
        <circle class="phone-ring" r="10"/>
        <path class="phone-handset" d="M-5,-6 l3,-1 l2,4 l-2,2 c1,3 3,5 6,6 l2,-2 l4,2 l-1,3 c-8,1 -15,-6 -14,-14 Z"/>
      </g>
      <text class="phone-number" x="527" y="274">555-613-2907</text>

      <text class="person-name" x="495" y="344">Marcus Delgado</text>
      <g class="phone-icon" transform="translate(506,377)">
        <circle class="phone-ring" r="10"/>
        <path class="phone-handset" d="M-5,-6 l3,-1 l2,4 l-2,2 c1,3 3,5 6,6 l2,-2 l4,2 l-1,3 c-8,1 -15,-6 -14,-14 Z"/>
      </g>
      <text class="phone-number" x="527" y="385">555-287-4163</text>
    </svg>
  </div>
</body>
</html>
```